Letterhead design - Harwick Group

We have just had our Logo created and our now wantng a letterhead design to incorporate this. Please use the same colours as in the logo, which is attached.
Please use the company details below
P O Box 86, Bleneheim 7315
Ph: 03 642 1937
dave@harwickgroup.co.nz
We would like a professional look
We need an overall letterhead design for our varied group of buisinesses which are based in NZ and overseas. We grow and develop buisinesses. Our companies began in NZ but we now have branches overseas as well. People are our greatest asset and we employ some incredible staff. Our buisinesses are scientific, innovative and growing in size and expertise with a financial base.

Target Market(s)

Professionals

Industry/Entity Type

Investment

Requirements
Must have
• Easy to read.
• Please use the same colours as in the logo
• Please use the company details below
• P O Box 86, Bleneheim 7315
• Ph: 03 642 1937
• dave@harwickgroup.co.nz

```html
<!DOCTYPE html>
<html lang="en">
<head>
<meta charset="utf-8">
<title>Harwick Group Letterhead</title>
<link href="https://fonts.googleapis.com/css2?family=Open+Sans:wght@400;600;700&display=swap" rel="stylesheet">
<style>
  :root {
    --backdrop: #e4e5e7;
    --paper: #f8f8f8;
    --brand-green: #22b573;
    --ink: #2b2b2b;
    --ink-soft: #3a3a3a;
    --mark-grey: #5a5a5a;
    --white: #ffffff;
  }
  html, body {
    margin: 0;
    padding: 0;
    width: 1200px;
    height: 945px;
    overflow: hidden;
    background: var(--backdrop);
    font-family: "Open Sans", Arial, sans-serif;
  }
  .letterhead {
    position: absolute;
    left: 280px;
    top: 20px;
    width: 640px;
    height: 905px;
    background: var(--paper);
    box-shadow: 0 4px 18px rgba(0,0,0,0.12);
    overflow: hidden;
  }
  .brand {
    position: absolute;
    top: 58px;
    left: 0;
    right: 0;
    display: flex;
    justify-content: center;
    align-items: center;
    gap: 10px;
  }
  .brand-square {
    width: 30px;
    height: 30px;
    background: var(--mark-grey);
  }
  .brand-name {
    font-size: 24px;
    font-weight: 700;
    color: var(--brand-green);
    letter-spacing: 0.5px;
    text-transform: uppercase;
  }
  .letter-body {
    position: absolute;
    top: 205px;
    left: 82px;
    width: 470px;
    color: var(--ink-soft);
    font-size: 11.6px;
    line-height: 15.5px;
  }
  .salutation {
    font-family: Arial, Helvetica, sans-serif;
    font-weight: 700;
    font-size: 13.5px;
    color: var(--ink);
    margin: 0 0 14px;
  }
  .letter-body p {
    margin: 0 0 17px;
    text-align: justify;
  }
  .signature {
    position: absolute;
    top: 660px;
    left: 100px;
    width: 140px;
    height: 48px;
    background: linear-gradient(90deg, #e6e6e6, #efefef);
  }
  .contact-band {
    position: absolute;
    bottom: 0;
    left: 120px;
    right: 0;
    height: 34px;
    box-sizing: border-box;
    background: var(--brand-green);
    color: var(--white);
    font-size: 9.5px;
    display: flex;
    align-items: center;
    justify-content: space-between;
    padding: 0 18px 0 26px;
    white-space: nowrap;
  }
  .contact-item {
    display: flex;
    align-items: center;
    gap: 4px;
  }
  .contact-item svg {
    width: 10px;
    height: 10px;
    fill: var(--white);
    flex: none;
  }
</style>
</head>
<body>
  <main class="letterhead">
    <header class="brand">
      <span class="brand-square"></span>
      <span class="brand-name">Harwick Group</span>
    </header>

    <section class="letter-body">
      <p class="salutation">Dear Mr. Hale,</p>
      <p>Lorem Ipsum is simply dummy text of the printing and typesetting industry. Lorem Ipsum has been the industry's standard dummy text ever since the 1500s, when an unknown printer took a galley of type and scrambled it to make a type specimen book. It has survived not only five centuries, but also the leap into electronic typesetting, remaining essentially unchanged.</p>
      <p>The standard chunk of Lorem Ipsum used since the 1500s is reproduced below for those interested. Sections 1.10.32 and 1.10.33 from "de Finibus Bonorum et Malorum" by Vellanus are also reproduced in their exact original form, accompanied by English versions from the 1914 translation by H. Denmore.</p>
      <p>Lorem Ipsum is simply dummy text of the printing and typesetting industry. Lorem Ipsum has been the industry's standard dummy text ever since the 1500s, when an unknown printer took a galley of type and scrambled it to make a type specimen book. It has survived not only five centuries, but also the leap into electronic typesetting, remaining essentially unchanged. It was popularised in the</p>
      <p>The standard chunk of Lorem Ipsum used since the 1500s is reproduced below for those interested. Sections 1.10.32 and 1.10.33 from "de Finibus Bonorum et Malorum" by Vellanus are also reproduced in their exact original form, accompanied by English versions from the 1914 translation by H. Denmore.</p>
      <p>The standard chunk of Lorem Ipsum used since the 1500s is reproduced below for those interested. Sections 1.10.32 and 1.10.33 from "de Finibus Bonorum et Malorum" by Vellanus are also reproduced in their exact original form.</p>
    </section>

    <div class="signature" role="img" aria-label="Handwritten signature of the sender"></div>

    <footer class="contact-band">
      <span class="contact-item">
        <svg viewBox="0 0 24 24" aria-hidden="true"><path d="M6.6 10.8a15.1 15.1 0 0 0 6.6 6.6l2.2-2.2c.3-.3.7-.4 1-.2 1.1.4 2.3.6 3.6.6.6 0 1 .4 1 1V20c0 .6-.4 1-1 1C10.6 21 3 13.4 3 4c0-.6.4-1 1-1h3.5c.6 0 1 .4 1 1 0 1.3.2 2.5.6 3.6.1.3 0 .7-.2 1l-2.3 2.2z"/></svg>
        03 642 1937
      </span>
      <span class="contact-item">
        <svg viewBox="0 0 24 24" aria-hidden="true"><path d="M2 5h20v14H2z M2 5l10 8 10-8" stroke="#22b573" stroke-width="1.5"/></svg>
        dave@harwickgroup.co.nz
      </span>
      <span class="contact-item">
        <svg viewBox="0 0 24 24" aria-hidden="true"><circle cx="12" cy="12" r="10"/></svg>
        www.harwickgroup.co.nz
      </span>
      <span class="contact-item">
        <svg viewBox="0 0 24 24" aria-hidden="true"><path d="M12 2a7 7 0 0 0-7 7c0 5.3 7 13 7 13s7-7.7 7-13a7 7 0 0 0-7-7zm0 9.5A2.5 2.5 0 1 1 12 6.5a2.5 2.5 0 0 1 0 5z"/></svg>
        P O Box 86, Bleneheim 7315
      </span>
    </footer>
  </main>
</body>
</html>
```